Tactical Supply Company needing memorable business card design

Our tactical supply comapny is in need of a new business card design that will set us apart from the amateurs. We sell tactical gear ranging from backpacks and range bags to apparel and other gear. We are looking for a sharp design that incorporates our logo, website, and name. Our colors are white, red, and black, or any combination of the three, preferably red and black.
I have attached our logo with our name underneath but I have also edited that design with the logo incorporated next to the name (attached).

Target Market(s)

Law enforcement, military, tactical

Industry/Entity Type

Business

Contact Information for Business Card

Include www.fernhollowprovisions-demo.com

Colors
000000
ec1f27
ffffff

Requirements
Must have
• Our name, logo, and website. This is intended to be a memorable simple card, no name, address, email, or phone number info is necessary. Designs that do include this additional info will still be considered if they are absolutely spectacular.
Should not have
• A standard template design, I can create that in my own on Cardvellum. I am looking for a new, creative design that is completely unique to my company.

```html
<!DOCTYPE html>
<html lang="en">
<head>
<meta charset="utf-8">
<title>Fernhollow Tactical Supply – Business Cards</title>
<link href="https://fonts.googleapis.com/css2?family=Exo+2:wght@700;800&family=Ubuntu:wght@500;700&display=swap" rel="stylesheet">
<style>
  :root {
    --page-bg: #e9e7e4;
    --card-light: #eeeeee;
    --card-mid: #d4d4d4;
    --card-dark: #b9b9b9;
    --ink: #2b2b2b;
    --red: #ec1f27;
    --groove: rgba(0,0,0,0.14);
    --groove-light: rgba(255,255,255,0.75);
  }
  * { box-sizing: border-box; margin: 0; padding: 0; }
  html, body { width: 1200px; height: 1000px; overflow: hidden; }
  body {
    background: var(--page-bg);
    position: relative;
    font-family: "Ubuntu", sans-serif;
  }
  .card {
    position: absolute;
    left: 320px;
    width: 560px;
    height: 320px;
    border-radius: 4px;
    background: linear-gradient(135deg, var(--card-light) 0%, var(--card-mid) 55%, var(--card-dark) 100%);
    box-shadow: 0 10px 28px rgba(0,0,0,0.18);
    overflow: hidden;
  }
  .card--back { top: 110px; }
  .card--front { top: 570px; }

  /* back */
  .back-brand {
    position: absolute; inset: 0;
    display: flex; flex-direction: column; align-items: center; justify-content: center;
    gap: 8px;
  }
  .brand-mark {
    width: 34px; height: 34px; background: var(--red); margin-bottom: 10px;
  }
  .brand-name {
    font-family: "Exo 2", sans-serif; font-weight: 800;
    color: var(--ink); font-size: 46px; letter-spacing: 2px; line-height: 1;
  }
  .brand-sub {
    font-family: "Exo 2", sans-serif; font-weight: 800;
    color: var(--ink); font-size: 15px; letter-spacing: 5px;
  }

  /* front */
  .groove {
    position: absolute; left: 0; right: 0; height: 2px;
    border-top: 1px solid var(--groove);
    border-bottom: 1px solid var(--groove-light);
  }
  .groove--top1 { top: 22px; }
  .groove--top2 { top: 30px; }
  .groove--bot1 { bottom: 30px; }
  .groove--bot2 { bottom: 22px; }

  .front-brand {
    position: absolute; left: 42px; top: 62px;
    display: flex; align-items: center; gap: 14px;
  }
  .front-brand .brand-mark { width: 40px; height: 40px; margin: 0; }
  .front-brand .brand-name { font-size: 40px; color: var(--red); }
  .front-brand .brand-sub { font-size: 12px; letter-spacing: 4px; margin-top: 4px; }

  .contact-list {
    position: absolute; left: 42px; top: 158px;
    list-style: none; display: flex; flex-direction: column; gap: 9px;
  }
  .contact-item {
    display: flex; align-items: center; gap: 12px;
    font-weight: 700; font-size: 17px; color: var(--ink);
  }
  .contact-icon {
    width: 20px; height: 20px; background: var(--red); border-radius: 3px; flex: none;
  }
</style>
</head>
<body>
  <section class="card card--back" aria-label="Card back">
    <div class="back-brand">
      <div class="brand-mark"></div>
      <div class="brand-name">FERNHOLLOW</div>
      <div class="brand-sub">TACTICAL SUPPLY</div>
    </div>
  </section>

  <section class="card card--front" aria-label="Card front">
    <div class="groove groove--top1"></div>
    <div class="groove groove--top2"></div>
    <div class="front-brand">
      <div class="brand-mark"></div>
      <div>
        <div class="brand-name">FERNHOLLOW</div>
        <div class="brand-sub">TACTICAL SUPPLY</div>
      </div>
    </div>
    <ul class="contact-list">
      <li class="contact-item"><span class="contact-icon"></span>www.fernhollowprovisions-demo.com</li>
      <li class="contact-item"><span class="contact-icon"></span>friendwall-demo.com/fernhollow</li>
      <li class="contact-item"><span class="contact-icon"></span>chirpline-demo.com/fernhollow</li>
      <li class="contact-item"><span class="contact-icon"></span>snapgrid-demo.com/fernhollowtactical</li>
    </ul>
    <div class="groove groove--bot1"></div>
    <div class="groove groove--bot2"></div>
  </section>
</body>
</html>
```